Monthly Wall Calendar for German shepherd Rescue

We will provide photo's description of dogs and placement of photos and all written material for calendar. We need a wall calendar and we will need as a final output pdf files with the proper bleed lines to send to printer. We have uploaded what the prior year calendar looked like. We are looking for something similar this year.

Generally there is a large monthly photo and 2-3 smaller ones added to the calendar page.

Target Market(s)

Our supporters and animal rescue people.

Font styles to use
Serif

Colors
6c459b
b7a5cd

Requirements
Must have
• A final pdf file with bleed lines for printer.
Nice to have
• The uploaded calendar gives a nice idea of what we are looking for as well as this link. http://brimleyhaven.com/calendar-2016-photo-spread/ and http://brimleyhaven.com/covers-2017/
Should not have
• Not cluttered

```html
<!DOCTYPE html>
<html lang="en">
<head>
<meta charset="utf-8">
<title>Brimley Haven Sanctuary – 2018 Wall Calendar</title>
<link rel="stylesheet" href="https://fonts.googleapis.com/css2?family=Stint+Ultra+Condensed&family=Open+Sans:wght@400;600;700&display=swap">
<style>
  :root {
    --purple: #6c459b;
    --purple-deep: #4e2f86;
    --lavender: #b7a5cd;
    --ink: #2e2e2e;
    --sky: #7fb0c4;
    --sky-soft: #a9c6e4;
    --grass: #7d7a3c;
    --forest: #4f5a2a;
    --grey-band: #d1d2d4;
    --blue: #1f5fa8;
    --cell: #e9e8f3;
    --cell-dark: #c3c6e3;
    --white: #ffffff;
    --display: "Stint Ultra Condensed", "Times New Roman", serif;
    --body: "Open Sans", Arial, sans-serif;
  }
  * { box-sizing: border-box; margin: 0; padding: 0; }
  html, body { width: 1200px; height: 1200px; overflow: hidden; background: var(--white); }
  .canvas { position: relative; width: 1200px; height: 1200px; font-family: var(--body); color: var(--ink); }

  /* ---------- Cover ---------- */
  .cover { position: absolute; left: 60px; top: 200px; width: 538px; height: 830px; border: 1px solid #555; overflow: hidden; }
  .cover svg { position: absolute; inset: 0; }
  .page-label { position: absolute; left: 548px; top: 1040px; font-size: 16px; color: #999; letter-spacing: .5px; }

  .display { position: absolute; font-family: var(--display); line-height: 1; white-space: nowrap; }
  .title-top { left: 324px; color: var(--white); }
  .title-top .l1 { position: absolute; top: 26px; font-size: 54px; }
  .title-top .l2 { position: absolute; top: 72px; font-size: 54px; }
  .title-top .l3 { position: absolute; top: 116px; font-size: 40px; }
  .title-bottom { left: 50px; color: var(--ink); }
  .title-bottom .l1 { position: absolute; top: 450px; font-size: 54px; }
  .title-bottom .l2 { position: absolute; top: 496px; font-size: 54px; }
  .title-bottom .l3 { position: absolute; top: 538px; font-size: 40px; }
  .cal-word { font-size: 44px; }
  .cal-year { font-size: 132px; }
  .cover .cal-word.top { left: 160px; top: 342px; color: var(--ink); }
  .cover .cal-year.top { left: 308px; top: 258px; color: var(--ink); }
  .cover .cal-word.bottom { left: 172px; top: 749px; color: var(--white); }
  .cover .cal-year.bottom { left: 322px; top: 666px; color: var(--white); }

  /* ---------- January page ---------- */
  .month-page { position: absolute; left: 626px; top: 203px; width: 537px; height: 830px; border: 1px solid #555; }
  .month-page > svg { position: absolute; left: -1px; top: -9px; overflow: visible; }
  .site-url { position: absolute; left: 22px; top: 28px; font-size: 13px; font-weight: 600; color: var(--ink); }
  .site-url b { color: var(--purple); font-weight: 700; }

  .sidebar-text { position: absolute; left: 398px; width: 120px; color: var(--white); text-align: center; }
  .sidebar-title { top: 30px; font-family: var(--display); font-size: 26px; line-height: 24px; }
  .sidebar-rule { position: absolute; left: 448px; top: 114px; width: 20px; height: 3px; background: var(--white); }
  .sidebar-copy { top: 133px; left: 404px; width: 108px; font-size: 7.6px; line-height: 10.9px; }

  .month-name { position: absolute; left: 98px; top: 512px; transform-origin: 0 0; transform: rotate(90deg); font-family: var(--display); font-size: 50px; color: var(--purple); line-height: 1; }
  .month-year { position: absolute; left: 56px; top: 512px; transform-origin: 0 0; transform: rotate(90deg); font-family: var(--display); font-size: 38px; color: var(--ink); line-height: 1; }
  .month-mark { position: absolute; left: 14px; top: 586px; width: 36px; height: 56px; border-radius: 40% 40% 45% 45%; background: linear-gradient(160deg, var(--lavender), var(--purple)); }

  .mini { position: absolute; left: 30px; width: 72px; }
  .mini h3 { font-size: 7.5px; font-weight: 700; border-bottom: 1px solid #999; padding-bottom: 1px; margin-bottom: 2px; }
  .mini h3 span { font-weight: 400; }
  .mini .days { display: grid; grid-template-columns: repeat(7, 10px); font-size: 5.2px; line-height: 9.8px; font-weight: 600; text-align: center; }
  .mini .days .we { color: var(--blue); }
  .mini.dec { top: 658px; }
  .mini.feb { top: 734px; }

  .grid { position: absolute; left: 102px; top: 512px; display: grid; grid-template-columns: repeat(7, 54px); column-gap: 6px; }
  .grid .head { height: 10px; background: var(--blue); color: var(--white); font-size: 5.5px; font-weight: 700; text-align: center; line-height: 10px; margin-bottom: 6px; }
  .grid .cell { position: relative; height: 51px; margin-bottom: 6px; background: var(--cell); }
  .grid .cell.we, .grid .cell.holiday { background: var(--cell-dark); }
  .grid .num { position: absolute; right: 3px; bottom: 1px; font-family: var(--display); font-size: 15px; color: var(--ink); line-height: 1; }
  .grid .cell.we .num, .grid .cell.holiday .num { color: var(--blue); }
  .grid .label { position: absolute; left: 4px; bottom: 4px; font-size: 4.6px; color: var(--ink); }
  .grid .photo { background: linear-gradient(180deg, var(--sky-soft) 0%, var(--grass) 100%); }
  .grid .photo.wide { grid-column: span 3; background: linear-gradient(90deg, var(--forest), #b9b68a 55%, var(--forest)); }
</style>
</head>
<body>
<div class="canvas">

  <!-- Cover -->
  <section class="cover">
    <svg width="538" height="830" viewBox="0 0 538 830">
      <defs>
        <linearGradient id="coverSky" x1="0" y1="0" x2="0" y2="1">
          <stop offset="0" stop-color="#a9c6e4"/>
          <stop offset=".55" stop-color="#c0986a"/>
          <stop offset="1" stop-color="#7d7a3c"/>
        </linearGradient>
        <linearGradient id="coverForest" x1="0" y1="0" x2="0" y2="1">
          <stop offset="0" stop-color="#4f5a2a"/>
          <stop offset=".5" stop-color="#6b5a3e"/>
          <stop offset="1" stop-color="#5d6b2c"/>
        </linearGradient>
      </defs>
      <polygon points="0,0 538,0 538,226 389,236 389,316 0,342" fill="var(--purple)"/>
      <polygon points="0,80 389,58 389,316 0,342" fill="url(#coverSky)" role="img" aria-label="Photo: German shepherd mother lying in grass with two puppies"/>
      <line x1="26" y1="416" x2="512" y2="416" stroke="#ccc" stroke-width="1" stroke-dasharray="2 3"/>
      <polygon points="0,604 538,458 538,830 0,830" fill="var(--purple)"/>
      <polygon points="150,563 538,458 538,720 150,746" fill="url(#coverForest)" role="img" aria-label="Photo: young German shepherd lying in the grass with tongue out"/>
    </svg>

    <div class="display title-top">
      <span class="l1">BRIMLEY</span>
      <span class="l2">HAVEN</span>
      <span class="l3">SANCTUARY</span>
    </div>
    <div class="display cal-word top">CALENDAR</div>
    <div class="display cal-year top">2018</div>

    <div class="display title-bottom">
      <span class="l1">BRIMLEY</span>
      <span class="l2">HAVEN</span>
      <span class="l3">SANCTUARY</span>
    </div>
    <div class="display cal-word bottom">CALENDAR</div>
    <div class="display cal-year bottom">2018</div>
  </section>
  <div class="page-label">COVER</div>

  <!-- January page -->
  <section class="month-page">
    <svg width="539" height="520" viewBox="0 0 539 520">
      <defs>
        <linearGradient id="lakeScene" x1="0" y1="0" x2="0" y2="1">
          <stop offset="0" stop-color="#78b3c6"/>
          <stop offset=".6" stop-color="#5b8a94"/>
          <stop offset="1" stop-color="#8a7f70"/>
        </linearGradient>
      </defs>
      <polygon points="1,9 538,9 538,43 1,81" fill="var(--grey-band)"/>
      <polygon points="1,84 538,46 538,475 1,515" fill="url(#lakeScene)" role="img" aria-label="Photo: German shepherd standing on a pebble beach beside a lake"/>
      <line x1="1" y1="82" x2="538" y2="44" stroke="#fff" stroke-width="2.5"/>
      <path d="M399,3 H519 V450 A60,60 0 0 1 399,450 Z" fill="var(--purple-deep)" opacity=".9"/>
      <circle cx="459" cy="444" r="48" fill="#7b8a3a" role="img" aria-label="Photo: German shepherd lying in grass"/>
    </svg>

    <div class="site-url">www.<b>brimleyhaven</b>.com</div>

    <div class="sidebar-text sidebar-title">LOREM<br>IPSUM</div>
    <div class="sidebar-rule"></div>
    <p class="sidebar-text sidebar-copy">Lorem ipsum dolor sit amet, consectetur adipiscing elit. Sed non dapibus eros. Quisque facilisis ultricies dignissim. In ultrices, mi vitae placerat cursus, diam nisi egestas eros, at dignissim arcu metus id eros. Aenean sem tellus, laoreet nec convallis sed, ultrices et tellus. Phasellus odio metus, pulvinar sed egestas in, mollis eget urna. Fusce sit amet ipsum tellus. Etiam luctus tristique purus, vel fringilla tellus sollicitudin a. Fusce dignissim aliquet semper.</p>

    <div class="month-name">JANUARY</div>
    <div class="month-year">2018</div>
    <div class="month-mark" role="img" aria-label="Illustration: German shepherd head"></div>

    <div class="mini dec">
      <h3>DECEMBER <span>2017</span></h3>
      <div class="days">
        <span class="we">S</span><span>M</span><span>T</span><span>W</span><span>T</span><span>F</span><span class="we">S</span>
        <span></span><span>1</span><span>2</span><span>3</span><span>4</span><span>5</span><span class="we">6</span>
        <span class="we">7</span><span>8</span><span>9</span><span>10</span><span>11</span><span>12</span><span class="we">13</span>
        <span class="we">14</span><span>15</span><span>16</span><span>17</span><span>18</span><span>19</span><span class="we">20</span>
        <span class="we">21</span><span>22</span><span>23</span><span>24</span><span>25</span><span>26</span><span class="we">27</span>
        <span class="we">28</span><span>29</span><span>30</span><span>31</span>
      </div>
    </div>
    <div class="mini feb">
      <h3>FEBRUARY <span>2018</span></h3>
      <div class="days">
        <span class="we">S</span><span>M</span><span>T</span><span>W</span><span>T</span><span>F</span><span class="we">S</span>
        <span></span><span></span><span></span><span></span><span>1</span><span>2</span><span class="we">3</span>
        <span class="we">4</span><span>5</span><span>6</span><span>7</span><span>8</span><span>9</span><span class="we">10</span>
        <span class="we">11</span><span>12</span><span>13</span><span>14</span><span>15</span><span>16</span><span class="we">17</span>
        <span class="we">18</span><span>19</span><span>20</span><span>21</span><span>22</span><span>23</span><span class="we">24</span>
        <span class="we">25</span><span>26</span><span>27</span><span>28</span>
      </div>
    </div>

    <div class="grid">
      <div class="head">SUN</div><div class="head">MON</div><div class="head">TUE</div><div class="head">WED</div><div class="head">THU</div><div class="head">FRI</div><div class="head">SAT</div>

      <div class="cell photo" role="img" aria-label="Photo: German shepherd by the water"></div>
      <div class="cell holiday"><span class="label">NEW YEARS DAY</span><span class="num">1</span></div>
      <div class="cell"><span class="num">2</span></div>
      <div class="cell"><span class="num">3</span></div>
      <div class="cell"><span class="num">4</span></div>
      <div class="cell"><span class="num">5</span></div>
      <div class="cell we"><span class="num">6</span></div>

      <div class="cell we"><span class="num">7</span></div>
      <div class="cell"><span class="num">8</span></div>
      <div class="cell"><span class="num">9</span></div>
      <div class="cell"><span class="num">10</span></div>
      <div class="cell"><span class="num">11</span></div>
      <div class="cell"><span class="num">12</span></div>
      <div class="cell we"><span class="num">13</span></div>

      <div class="cell we"><span class="num">14</span></div>
      <div class="cell holiday"><span class="label">M L KING DAY</span><span class="num">15</span></div>
      <div class="cell"><span class="num">16</span></div>
      <div class="cell"><span class="num">17</span></div>
      <div class="cell"><span class="num">18</span></div>
      <div class="cell"><span class="num">19</span></div>
      <div class="cell we"><span class="num">20</span></div>

      <div class="cell we"><span class="num">21</span></div>
      <div class="cell"><span class="num">22</span></div>
      <div class="cell"><span class="num">23</span></div>
      <div class="cell"><span class="num">24</span></div>
      <div class="cell"><span class="num">25</span></div>
      <div class="cell"><span class="num">26</span></div>
      <div class="cell we"><span class="num">27</span></div>

      <div class="cell we"><span class="num">28</span></div>
      <div class="cell"><span class="num">29</span></div>
      <div class="cell"><span class="num">30</span></div>
      <div class="cell"><span class="num">31</span></div>
      <div class="cell photo wide" role="img" aria-label="Photo: German shepherd sitting among sunlit trees"></div>
    </div>
  </section>

</div>
</body>
</html>
```